Pest Control Company needs business card!

Hi there, we need a business card designed for our new Pest Control Company. Ideally this card will be simple, yet feel elegant and high end. We want to use the colours Orange, Black and White. Please see our attached logo for the exact colours.

Business card details:

Phone - 0461 275 804
Name - Gavin Holloway
Email - Info@steadfastverminguard.com.au

We would also like to include the following list with dot points:

SERVICES / INSPECTIONS

Termites, Wood Borers, Ants, Cockroaches, Spiders, Fleas, Mice, Rats, Bed Bugs, & More!

```html
<!DOCTYPE html>
<html lang="en">
<head>
<meta charset="utf-8">
<title>Steadfast Vermin Guard – Business Card</title>
<link rel="stylesheet" href="https://fonts.googleapis.com/css2?family=Poppins:wght@400;700;800&display=swap">
<style>
  :root {
    --orange: #f47b14;
    --black: #121212;
    --black-soft: #1e1e1e;
    --white: #ffffff;
    --ink: #111111;
    --stage: #7f7f7f;
  }
  * { margin: 0; padding: 0; box-sizing: border-box; }
  html, body {
    width: 945px; height: 1200px; overflow: hidden;
    background: var(--stage);
    font-family: "Poppins", sans-serif;
  }
  .canvas { position: relative; width: 945px; height: 1200px; }

  .card {
    position: absolute; left: 71px; width: 793px; height: 453px;
    overflow: hidden;
    background: radial-gradient(ellipse at 55% 45%, var(--black-soft) 0%, var(--black) 75%);
  }
  .card--front { top: 86px; }
  .card--back { top: 619px; }

  /* Front */
  .brand {
    position: absolute; left: 145px; top: 108px;
    color: var(--orange);
    font-weight: 800; font-size: 56px; line-height: 66px;
    text-transform: uppercase; letter-spacing: -1px;
  }
  .brand-dot {
    position: absolute; left: 540px; top: 150px;
    width: 130px; height: 130px; border-radius: 50%;
    background: var(--orange);
  }

  /* Back */
  .services-panel {
    position: absolute; left: 0; top: 0; width: 374px; height: 100%;
    background: var(--white);
  }
  .services-title {
    position: absolute; left: 42px; top: 50px;
    font-weight: 800; font-size: 29px; color: var(--ink); letter-spacing: -0.5px;
  }
  .title-mark { position: absolute; top: 53px; height: 24px; }
  .title-mark--black { left: 0; width: 13px; background: var(--ink); }
  .title-mark--orange { left: 18px; width: 19px; background: var(--orange); }

  .services-list {
    position: absolute; left: 18px; top: 101px; list-style: none;
  }
  .services-list li {
    position: relative; padding-left: 31px;
    font-size: 24px; line-height: 34px; color: var(--ink);
  }
  .services-list li::before {
    content: ""; position: absolute; left: 0; top: 9px;
    width: 17px; height: 17px; border-radius: 50%; background: var(--orange);
  }

  .icon-rail-back {
    position: absolute; left: 345px; top: 178px; width: 29px; height: 240px;
    background: var(--ink);
  }
  .icon-rail {
    position: absolute; left: 316px; top: 192px; width: 58px; height: 212px;
    background: var(--orange);
  }
  .icon { position: absolute; left: 14px; width: 32px; height: 32px; }
  .icon--person { top: 36px; }
  .icon--phone { top: 109px; }
  .icon--mail { top: 161px; }

  .person-name {
    position: absolute; left: 390px; top: 220px;
    font-weight: 700; font-size: 38px; letter-spacing: -0.5px;
    text-transform: uppercase; color: var(--white); white-space: nowrap;
  }
  .person-name .first { color: var(--orange); }
  .contact {
    position: absolute; left: 390px;
    font-size: 20px; color: var(--white); white-space: nowrap;
  }
  .contact--phone { top: 304px; }
  .contact--email { top: 353px; }
</style>
</head>
<body>
<main class="canvas">

  <section class="card card--front">
    <div class="brand">Steadfast<br>Vermin<br>Guard</div>
    <div class="brand-dot"></div>
  </section>

  <section class="card card--back">
    <div class="services-panel">
      <span class="title-mark title-mark--black"></span>
      <span class="title-mark title-mark--orange"></span>
      <h2 class="services-title">SERVICES</h2>
      <ul class="services-list">
        <li>TERMITES</li>
        <li>WOOD BORERS</li>
        <li>ANTS</li>
        <li>COCKROACHES</li>
        <li>SPIDERS</li>
        <li>FLEAS</li>
        <li>MICE</li>
        <li>RATS</li>
        <li>BED BUGS &amp; MORE!</li>
      </ul>
    </div>

    <div class="icon-rail-back"></div>
    <div class="icon-rail">
      <svg class="icon icon--person" viewBox="0 0 32 32" aria-hidden="true">
        <circle cx="16" cy="10" r="7" fill="#111"/>
        <path d="M2 30c0-7 6-11 14-11s14 4 14 11z" fill="#111"/>
      </svg>
      <svg class="icon icon--phone" viewBox="0 0 32 32" aria-hidden="true">
        <path d="M8 2l5 7-3 3c1.5 4 5 8 10 10l3-3 7 5-3 5C17 29 3 15 3 5z" fill="#111"/>
      </svg>
      <svg class="icon icon--mail" viewBox="0 0 32 32" aria-hidden="true">
        <rect x="2" y="7" width="28" height="19" fill="none" stroke="#111" stroke-width="2.5"/>
        <path d="M2 7l14 11L30 7M2 26l10-9M30 26l-10-9" fill="none" stroke="#111" stroke-width="2"/>
      </svg>
    </div>

    <h1 class="person-name"><span class="first">Gavin</span> Holloway</h1>
    <p class="contact contact--phone">0461 275 804</p>
    <p class="contact contact--email">Info@steadfastverminguard.com.au</p>
  </section>

</main>
</body>
</html>
```